Funky Cloud Security Startup wants a cutting edge website

We're looking for a clean and simple website to be able to sell out cutting edge Cloud Security products. We already have a logo and business codes to give you a view of the style/colours etc (see attached). Really looking for something similar to brimlo.com , vadrine.com and if push comes to shove then our competitors tandry pelwick.com.au don't have a bad site either.

We're still working through the content sections but want to have a home for the following types of content immediately:

Products (4 of them)
Company
Technology Partners
Press/News
Contact Us
Support
Login

and the site will need to expand to accommodate

Buy
Case Studies
Channel Partners

at some point in the future

On the bottom Nav we want:
* Privacy Policy
* Terms of Use
* Contact
* Vantiqo
* Plimsy

The home page should an image rotator on it with some suitably cool images and call to actions as text hovering over them.

We need it to be easily editable in dreamweaver so a template is a must, it should also be completely CSS driven and adaptive so will work on mobile, tablet and desktop - you know the score.

We're hosting on a linux server so PHP code for any crazy stuff is a must.

Really exciting project as this will be a huge company with major investors backing it internationally so you will be able to put your name against the next Quorvix/Plimsy/Zembro.

Go crazy with your creativity, just remember kurvo's slogan is "Security made simple"

We look forward to seeing your creations, good luck!

```html
<!DOCTYPE html>
<html lang="en">
<head>
<meta charset="utf-8">
<title>kurvo — security made simple</title>
<link rel="stylesheet" href="https://fonts.googleapis.com/css2?family=Roboto:wght@300;400;700&family=Arimo:wght@400;700&display=swap">
<style>
:root{
  --ink:#3b3b3b;
  --white:#ffffff;
  --nav-top:#3aa6dc;
  --nav-bottom:#1b7fb5;
  --hero-bg:#5d5d5d;
  --accent-blue:#2a90c8;
  --accent-green:#a8d03a;
  --contact-green:#b3d443;
  --strip-grey:#ececec;
  --rule:#d3d3d3;
  --footer:#4a4a4a;
  --footer-text:#e6e6e6;
  --send:#5b5b5b;
}
*{box-sizing:border-box;margin:0;padding:0}
html,body{width:1200px;height:2375px;overflow:hidden}
body{position:relative;background:var(--white);font-family:"Roboto",Arial,sans-serif;color:var(--ink)}
section,header,nav,footer{position:absolute;left:0;width:1200px}

/* brand lockup */
.brand{display:flex;align-items:center;gap:12px;white-space:nowrap}
.brand-dot{width:34px;height:34px;border-radius:50%;background:var(--accent-blue)}
.brand-name{font-size:54px;font-weight:400;color:var(--ink);letter-spacing:1px;line-height:1}

/* header */
.site-header{top:0;height:104px}
.site-header .brand{position:absolute;left:132px;top:28px}
.slogan{position:absolute;right:138px;top:42px;font-size:34px;font-weight:300;color:#555;white-space:nowrap}

/* navigation */
.main-nav{top:104px;height:43px;background:linear-gradient(var(--nav-top),var(--nav-bottom));border-bottom:2px solid #146b99}
.main-nav ul{list-style:none;display:flex;position:absolute;left:135px;top:11px}
.main-nav li{font-size:15px;color:var(--white);font-weight:300;margin-right:38px;white-space:nowrap}

/* hero */
.hero{top:147px;height:391px;background:var(--hero-bg)}
.hero-art{position:absolute;left:160px;top:26px;width:356px;height:350px;border-radius:46% 46% 30% 30%;background:radial-gradient(circle at 45% 40%,#4aa6ee,#1c6fc4 55%,#7b7b7b 80%,transparent 81%)}
.hero-copy{position:absolute;left:579px;top:62px;width:500px;font-size:32px;font-weight:300;line-height:37px;color:var(--white)}
.btn{position:absolute;display:flex;align-items:center;gap:8px;padding:0 12px;height:36px;font-size:25px;font-weight:300;color:var(--white);white-space:nowrap}
.btn svg{width:20px;height:20px;flex:none}
.hero .btn{left:582px;top:238px;background:var(--accent-green)}
.slide-dots{position:absolute;left:1002px;top:364px;display:flex;gap:4px}
.slide-dots span{width:14px;height:14px;background:var(--accent-blue)}
.slide-dots span.is-active{background:var(--accent-green)}

/* products */
.products{top:538px;height:353px}
.product{position:absolute;top:60px;width:240px;text-align:center}
.product-art{width:135px;height:130px;margin:0 auto;border-radius:24px;background:linear-gradient(#5cb8ef,#1d78c6)}
.product-art.dark{background:linear-gradient(#6a6a6a,#1c1c1c)}
.product h3{margin-top:26px;font-size:22px;font-weight:300;color:var(--accent-blue);white-space:nowrap}
.product p{margin:10px auto 0;width:200px;font-family:"Arimo",Arial,sans-serif;font-size:12.5px;line-height:15px;color:var(--ink);text-align:left}

/* about */
.about{top:891px;height:412px;background:#000}
.about-photo{position:absolute;left:0;top:0;width:1200px;height:412px;background:radial-gradient(ellipse at 35% 55%,#5c6a78,#1d232a 45%,#000 75%)}
.about h2{position:absolute;left:612px;top:40px;font-size:64px;font-weight:300;color:var(--white);letter-spacing:-1px;white-space:nowrap}
.about p{position:absolute;left:612px;top:140px;width:470px;font-size:20px;font-weight:300;line-height:28.5px;color:var(--white)}
.about .btn{left:612px;top:312px;background:var(--accent-blue)}

/* client names */
.clients{top:1303px;height:119px;background:var(--strip-grey)}
.clients-row{position:absolute;left:160px;top:30px;width:878px;height:60px;border-top:1px solid var(--rule);border-bottom:1px solid var(--rule);display:flex;justify-content:space-between;align-items:center}
.client{font-size:21px;font-weight:700;color:#555;display:flex;align-items:center;gap:6px}
.client i{width:14px;height:14px;border-radius:50%;background:#666}

/* news */
.news{top:1422px;height:307px}
.news h2{position:absolute;left:0;width:1200px;top:46px;text-align:center;font-size:22px;font-weight:300;color:var(--ink)}
.news-item{position:absolute;top:107px;width:220px}
.date{position:absolute;left:0;top:0;width:73px;height:89px;background:var(--accent-blue);color:var(--white);text-align:center}
.date::after{content:"";position:absolute;right:-12px;top:14px;border-left:12px solid var(--accent-blue);border-top:10px solid transparent;border-bottom:10px solid transparent}
.date b{display:block;font-size:38px;font-weight:300;padding-top:12px;line-height:40px}
.date small{font-size:15px}
.news-text{position:absolute;left:95px;top:0;width:122px;font-family:"Arimo",Arial,sans-serif}
.news-text h3{font-size:12.5px;line-height:13px;font-weight:700;color:#222}
.news-text p{margin-top:4px;font-size:12.5px;line-height:13.5px;color:#444}

/* contact */
.contact{top:1729px;height:424px;background:var(--contact-green);color:var(--white)}
.contact h2{position:absolute;left:0;width:1200px;top:48px;text-align:center;font-size:44px;font-weight:300}
.contact-intro{position:absolute;left:0;width:1200px;top:106px;text-align:center;font-size:20px;font-weight:300;line-height:25px}
.field{position:absolute;background:var(--white);font-family:"Arimo",Arial,sans-serif;font-size:14px;color:#444;padding:13px 16px}
.send{position:absolute;left:614px;top:304px;width:394px;height:44px;background:var(--send);display:flex;align-items:center;justify-content:center}

/* footer */
.site-footer{top:2153px;height:222px;background:var(--footer);color:var(--footer-text)}
.footer-col{position:absolute;top:46px}
.footer-col h4{font-size:21px;font-weight:300;color:var(--white);margin-bottom:14px;white-space:nowrap}
.footer-links{display:flex;gap:22px;font-family:"Arimo",Arial,sans-serif;font-size:12.5px;line-height:17.5px}
.footer-links ul{list-style:none;width:120px;white-space:nowrap}
.social{list-style:none;font-family:"Arimo",Arial,sans-serif;font-size:14px;line-height:28px}
.social li{display:flex;align-items:center;gap:10px}
.social i{width:20px;height:20px;border-radius:50%;background:#9a9a9a}
.footer-address{font-family:"Arimo",Arial,sans-serif;font-size:12px;line-height:14px;white-space:nowrap}
.footer-phone{display:flex;align-items:center;gap:6px;margin-top:10px;font-size:23px;font-weight:300;color:#cfcfcf;white-space:nowrap}
.footer-brand{position:absolute;left:820px;top:48px}
.footer-brand .brand-dot{background:var(--white);width:28px;height:28px}
.footer-brand .brand-name{color:var(--white);font-size:48px}
.footer-brand p{margin-top:12px;margin-left:4px;font-family:"Arimo",Arial,sans-serif;font-size:12px;line-height:14px}
</style>
</head>
<body>

<header class="site-header">
  <div class="brand"><span class="brand-dot"></span><span class="brand-name">kurvo.</span></div>
  <div class="slogan">security made simple</div>
</header>

<nav class="main-nav">
  <ul>
    <li>company</li><li>technology partners</li><li>press/news</li><li>contact us</li><li>support</li><li>buy</li><li>case studies</li><li>channel partners</li><li>login</li>
  </ul>
</nav>

<section class="hero">
  <div class="hero-art" role="img" aria-label="Illustration of a glossy blue cloud guarded by a red and yellow shield"></div>
  <p class="hero-copy">Lorem ipsum dolor sit amet, consectetur adipisicing elit, sed do eiusmod tempor incididunt ut labore et dolore magna aliqua.</p>
  <div class="btn"><svg viewBox="0 0 20 20"><circle cx="10" cy="10" r="9" fill="#fff"/><path d="M5 10h8M10 6l4 4-4 4" stroke="var(--accent-green)" stroke-width="2.4" fill="none"/></svg>more info</div>
  <div class="slide-dots"><span class="is-active"></span><span></span><span></span><span></span></div>
</section>

<section class="products">
  <div class="product" style="left:103px">
    <div class="product-art" role="img" aria-label="Icon of a blue game controller"></div>
    <h3>secured gaming</h3>
    <p>Duis aute irure dolor in reprehendrit in voluptate velit esse cillum dolore eu fugiat nulla pariatur.</p>
  </div>
  <div class="product" style="left:353px">
    <div class="product-art" role="img" aria-label="Icon of a cloud with an upload arrow over a media player"></div>
    <h3>safe cloud media</h3>
    <p>Excepteur sint occaecat cupidatat non proident, sunt in cua qui officia deserunt mollit anim idborum.</p>
  </div>
  <div class="product" style="left:592px">
    <div class="product-art dark" role="img" aria-label="Icon of a mobile phone showing a cloud sync arrow"></div>
    <h3>secured mobile</h3>
    <p>Sed ut perspiciatis, unde omnis iste natus error sit voluptatem accusantium doloremque laud.</p>
  </div>
  <div class="product" style="left:844px">
    <div class="product-art dark" role="img" aria-label="Icon of a stacked server unit with a cloud on top"></div>
    <h3>cloud hosting</h3>
    <p>Nemo enim ipsam voluptatem, quia voluptas sit, aspernatur aut odit aut fugit, sed quia.</p>
  </div>
</section>

<section class="about">
  <div class="about-photo" role="img" aria-label="Photo of a person in a suit holding a glass tablet showing a cloud network diagram"></div>
  <h2>who is kurvo?</h2>
  <p>At vero eos et accusamus et iusto odio dignissimos ducimus, qui blanditiis praesentium voluptatum deleniti atque corrupti, quos dolores et quas molestias excepturi sint, obcaecati cupiditate non provident, similique sunt in culpa.</p>
  <div class="btn"><svg viewBox="0 0 20 20"><circle cx="10" cy="10" r="9" fill="#fff"/><path d="M5 10h8M10 6l4 4-4 4" stroke="var(--accent-blue)" stroke-width="2.4" fill="none"/></svg>more info</div>
</section>

<section class="clients">
  <div class="clients-row">
    <span class="client"><i></i>Haltrex</span>
    <span class="client">Vexmar</span>
    <span class="client">Aerolyn</span>
    <span class="client">Olvenne</span>
    <span class="client">Sternholt</span>
    <span class="client">Telvana</span>
    <span class="client">Vexmar</span>
  </div>
</section>

<section class="news">
  <h2>press / news</h2>
  <article class="news-item" style="left:144px">
    <div class="date"><b>12</b><small>NOV</small></div>
    <div class="news-text"><h3>LOREM IPSUM DOLOR AMET</h3><p>Psum dolor sit amet, consectetuer adipiscing elit, sed diam nonummy nibh euismod.</p></div>
  </article>
  <article class="news-item" style="left:380px">
    <div class="date"><b>04</b><small>NOV</small></div>
    <div class="news-text"><h3>EXCEPTEUR SINT OCCAECAT CUPID</h3><p>Duis aute irure dolor in reprehderit in voluptate velit esse cillum dolore eu fugiat nulla pariatur.</p></div>
  </article>
  <article class="news-item" style="left:614px">
    <div class="date"><b>27</b><small>OCT</small></div>
    <div class="news-text"><h3>NEMO ENIM IPSAM VOLUPTATEM</h3><p>Excepteur sint occa ecat cupidatat non proident, sunt in cua qui officia deserunt mollit anim idborum.</p></div>
  </article>
  <article class="news-item" style="left:850px">
    <div class="date"><b>15</b><small>OCT</small></div>
    <div class="news-text"><h3>DUIS AUTE IRURE DOLOR IN REPRE</h3><p>Nemo enim ipsam voluptatem, quia voluptas sit, aspernatur aut odit aut fugit, sed quia.</p></div>
  </article>
</section>

<section class="contact">
  <h2>contact us</h2>
  <p class="contact-intro">We'd really love to hear from you so why not give us a call on 1300 482 615 or<br>drop us an email and we'll get back to you as soon as we can.</p>
  <div class="field" style="left:192px;top:185px;width:394px;height:46px">Full Name</div>
  <div class="field" style="left:192px;top:243px;width:394px;height:46px">Email Address</div>
  <div class="field" style="left:192px;top:304px;width:394px;height:46px">Phone Number</div>
  <div class="field" style="left:614px;top:185px;width:394px;height:104px">Message</div>
  <div class="send"><svg width="34" height="24" viewBox="0 0 34 24"><rect x="1" y="1" width="32" height="22" fill="none" stroke="#fff" stroke-width="2"/><path d="M1 1l16 12L33 1M1 23l12-11M33 23L21 12" fill="none" stroke="#fff" stroke-width="2"/></svg></div>
</section>

<footer class="site-footer">
  <div class="footer-col" style="left:139px">
    <h4>NAVIGATION</h4>
    <div class="footer-links">
      <ul><li>Home</li><li>Company</li><li>Technology Partners</li><li>Press/News</li><li>Contact Us</li><li>Support</li></ul>
      <ul><li>Buy</li><li>Case Studies</li><li>Channel Partners</li><li>Login</li><li>Privacy Policy</li><li>Terms of Use</li></ul>
    </div>
  </div>
  <div class="footer-col" style="left:420px">
    <h4>CONNECT</h4>
    <ul class="social"><li><i></i>Quorvix</li><li><i></i>Plimsy</li><li><i></i>Vantiqo</li></ul>
  </div>
  <div class="footer-col" style="left:632px">
    <h4>CONTACT US</h4>
    <p class="footer-address">#38 street city, state, Country<br>email : info@ornical.com.au</p>
    <div class="footer-phone"><svg width="26" height="26" viewBox="0 0 26 26"><circle cx="13" cy="13" r="11.5" fill="none" stroke="#cfcfcf" stroke-width="2"/><path d="M9 7c-1 1-1.5 2.5 0 5.5s4 5.5 6.5 6.5c1.5.5 2.5 0 3-1l-2.5-2.5-1.5 1c-1.5-.8-3-2.5-3.8-4l1-1.5z" fill="#cfcfcf"/></svg>014.762.3095</div>
  </div>
  <div class="footer-brand">
    <div class="brand"><span class="brand-dot"></span><span class="brand-name">kurvo.</span></div>
    <p>© Copyright kurvo. 2013.<br>All Rights Reserved</p>
  </div>
</footer>

</body>
</html>
```